Simple, Professional and neat business card design for Vendralo Inc.

We're looking to re-vamp our business card design. We're a supplier of innovative feed ingredients for the North American animal agriculture industry. We are located in Lucknow, Ontario, Canada and our flagship product is a product that prevents milk fever in dairy cows when the calve, it is fed before calving and is very effective compared to other alternatives available on the market today.

Our company has Danish roots and we import all of our product from our Danish partner/manufacturer in Denmark. We like our design to embrace high professionalism while remaining neat and simple.

Target Market(s)

B2B, Feed Mills, Veterinary Clinics, Large integrators/producers,

Industry/Entity Type

Agribusiness

Contact Information for Business Card

We like the rounded corners because they make the card easy to sit in a wallet and not many use it so it makes the card stand out, just possibly something to take account for during the design.

As you can also see on the sliders below, looking for a that simple but proffesional scandinavian design.

Requirements
Nice to have
• Rounded corners
Should not have
• Too vibrant

```html
<!DOCTYPE html>
<html lang="en">
<head>
<meta charset="utf-8">
<title>Vendralo Inc. business cards</title>
<link rel="stylesheet" href="https://fonts.googleapis.com/css2?family=Lato:wght@300;400;900&family=Open+Sans:wght@400;700&display=swap">
<style>
  :root{
    --bg:#3a3b3e;
    --navy:#1c3a8c;
    --blue:#1556ae;
    --ink:#14204a;
    --sky:#9ed6f1;
    --sky-soft:#d9f0fb;
    --tan:#e2c48d;
    --white:#ffffff;
  }
  *{margin:0;padding:0;box-sizing:border-box}
  html,body{width:1200px;height:974px;overflow:hidden;background:var(--bg)}
  .card{position:absolute;width:700px;height:400px;border-radius:44px;overflow:hidden;box-shadow:0 14px 30px rgba(0,0,0,.45)}

  /* info side */
  .card--info{left:60px;top:50px;background:radial-gradient(ellipse at 50% 40%,var(--sky-soft) 0%,var(--sky) 85%)}
  .brand-row{position:absolute;left:70px;top:52px;display:flex;align-items:center;gap:18px}
  .brand-dot{width:40px;height:40px;border-radius:50%;background:var(--blue)}
  .brand-name{font-family:"Lato",sans-serif;font-weight:900;font-size:50px;color:var(--blue);letter-spacing:.5px}
  .rule{position:absolute;height:1px;background:var(--navy);opacity:.45}
  .rule--top{left:60px;right:60px;top:132px}
  .rule--bottom{left:60px;right:60px;top:222px}
  .tagline{position:absolute;left:70px;top:146px;width:580px;font-family:"Open Sans",sans-serif;font-weight:700;font-size:22px;line-height:30px;color:var(--ink)}
  .features{position:absolute;left:40px;right:40px;top:236px;display:flex;justify-content:space-between}
  .feature{width:200px;display:flex;flex-direction:column;align-items:center;gap:12px}
  .feature svg{width:96px;height:96px}
  .pill{font-family:"Open Sans",sans-serif;font-size:17px;color:var(--ink);border:1.5px solid var(--blue);border-radius:20px;padding:2px 16px;background:rgba(255,255,255,.35);white-space:nowrap}

  /* contact side */
  .card--contact{left:440px;top:520px;background:linear-gradient(115deg,var(--white) 25%,var(--sky) 100%)}
  .mark{position:absolute;left:40px;top:60px;width:280px;display:flex;flex-direction:column;align-items:center;gap:22px}
  .mark-circle{width:150px;height:150px;border-radius:50%;background:var(--tan)}
  .mark-name{font-family:"Lato",sans-serif;font-weight:900;font-size:36px;color:var(--blue);white-space:nowrap}
  .divider{position:absolute;left:345px;top:40px;width:1px;height:270px;background:var(--navy);opacity:.6}
  .person{position:absolute;left:372px;top:44px;font-family:"Lato",sans-serif;font-size:27px;color:var(--navy);letter-spacing:.3px;white-space:nowrap}
  .person b{font-weight:900}
  .person span{font-weight:300}
  .rule--name{left:372px;right:40px;top:86px}
  .contacts{position:absolute;left:380px;top:100px;list-style:none;font-family:"Open Sans",sans-serif;font-size:16px;color:var(--ink)}
  .contacts li{display:flex;align-items:center;gap:12px;height:30px}
  .contacts svg{width:16px;height:16px;fill:var(--navy)}
  .band{position:absolute;left:0;bottom:0;width:700px;height:100px}
  .address{position:absolute;left:170px;bottom:22px;display:flex;align-items:center;gap:12px;font-family:"Open Sans",sans-serif;font-weight:700;font-size:20px;color:var(--white);white-space:nowrap}
  .address svg{width:16px;height:20px;fill:var(--white)}
</style>
</head>
<body>

<section class="card card--info">
  <div class="brand-row">
    <div class="brand-dot"></div>
    <div class="brand-name">VENDRALO INC.</div>
  </div>
  <div class="rule rule--top"></div>
  <p class="tagline">Distributor of innovative feed ingredients and other preventative health products.</p>
  <div class="rule rule--bottom"></div>

  <div class="features">
    <div class="feature">
      <svg viewBox="0 0 100 100" aria-hidden="true">
        <path d="M50 6 L88 20 C88 55 75 80 50 94 C25 80 12 55 12 20 Z" fill="var(--blue)" stroke="var(--navy)" stroke-width="4"/>
        <path d="M50 18 L78 28 C78 55 68 73 50 84 C32 73 22 55 22 28 Z" fill="none" stroke="#fff" stroke-width="3"/>
        <circle cx="50" cy="48" r="13" fill="#fff"/>
        <path d="M50 41 V55 M43 48 H57" stroke="var(--navy)" stroke-width="4"/>
      </svg>
      <span class="pill">Preventative Care</span>
    </div>
    <div class="feature">
      <svg viewBox="0 0 100 100" aria-hidden="true">
        <path d="M78 30 A38 38 0 1 0 70 82" fill="none" stroke="var(--ink)" stroke-width="6" stroke-dasharray="4 6"/>
        <path d="M50 50 L54 24 L58 50 Z" fill="var(--ink)"/>
        <circle cx="54" cy="52" r="6" fill="var(--ink)"/>
        <path d="M52 84 L66 62 L76 74 L92 44" fill="none" stroke="var(--blue)" stroke-width="7"/>
        <path d="M82 42 L96 38 L94 52 Z" fill="var(--blue)"/>
      </svg>
      <span class="pill">High-performance</span>
    </div>
    <div class="feature">
      <svg viewBox="0 0 100 100" aria-hidden="true">
        <circle cx="50" cy="50" r="44" fill="var(--blue)" stroke="var(--navy)" stroke-width="5"/>
        <text x="50" y="64" text-anchor="middle" font-family="Georgia,serif" font-weight="700" font-size="42" fill="#fff">Rx</text>
        <path d="M22 80 L78 20" stroke="var(--navy)" stroke-width="6"/>
      </svg>
      <span class="pill">Prescription-free</span>
    </div>
  </div>
</section>

<section class="card card--contact">
  <div class="mark">
    <div class="mark-circle"></div>
    <div class="mark-name">VENDRALO INC.</div>
  </div>
  <div class="divider"></div>
  <div class="person"><b>ANDERS</b> <span>HOLMGAARD</span></div>
  <div class="rule rule--name"></div>
  <ul class="contacts">
    <li><svg viewBox="0 0 16 16"><path d="M1 3h14v10H1z M1 3l7 6 7-6" /></svg>anders@vendralo.com</li>
    <li><svg viewBox="0 0 16 16"><circle cx="8" cy="8" r="7"/></svg>www.vendralo.com</li>
    <li><svg viewBox="0 0 16 16"><path d="M3 1l3 3-2 2c1 2 3 4 5 5l2-2 3 3-2 3C6 14 2 10 1 3z"/></svg>555-214-0381</li>
    <li><svg viewBox="0 0 16 16"><path d="M2 5c3-3 9-3 12 0l-2 2-2-1V5H6v1L4 7z M4 9h8l1 5H3z"/></svg>555-214-7620</li>
    <li><svg viewBox="0 0 16 16"><path d="M3 1l3 3-2 2c1 2 3 4 5 5l2-2 3 3-2 3C6 14 2 10 1 3z"/></svg>800-555-0147</li>
    <li><svg viewBox="0 0 16 16"><path d="M4 1h6l2 2v4H4z M2 7h12v8H2z"/></svg>555-214-7699</li>
  </ul>

  <svg class="band" viewBox="0 0 700 100" preserveAspectRatio="none" aria-hidden="true">
    <rect x="0" y="40" width="700" height="60" fill="var(--tan)"/>
    <polygon points="130,100 150,40 580,40 700,0 700,100" fill="var(--blue)"/>
    <path d="M126 100 L146 40" stroke="var(--tan)" stroke-width="3"/>
  </svg>
  <div class="address">
    <svg viewBox="0 0 16 20"><path d="M8 0a7 7 0 0 1 7 7c0 5-7 13-7 13S1 12 1 7a7 7 0 0 1 7-7z"/><circle cx="8" cy="7" r="2.5" fill="var(--blue)"/></svg>
    Box 240, Maplebrook, Ontario Canada N0X 1A0
  </div>
</section>

</body>
</html>
```